We are in search of a new business card design for our business. We have a Mexican Grocery Store called Tamarindo Market, we would like to see that some have mexican design, but we are open to any type of designs.

Phone: to be announced
Fax: to be announced

Address is:
2465 Calloway Blvd
Larkfield, MD 21290

Industry/Entity Type

Business

```html
<!DOCTYPE html>
<html lang="en">
<head>
<meta charset="utf-8">
<title>Tamarindo Market – Business Card</title>
<link href="https://fonts.googleapis.com/css2?family=Lato:wght@400;700&display=swap" rel="stylesheet">
<style>
  :root {
    --page: #e9e6e1;
    --card-white: #ffffff;
    --card-black: #1d1e20;
    --accent-red: #d8262c;
    --name-yellow: #f5cf16;
    --text-light: #e8e8e8;
    --text-muted: #c9c9c9;
  }
  * { margin: 0; padding: 0; box-sizing: border-box; }
  html, body {
    width: 1200px; height: 1022px; overflow: hidden;
    background: var(--page);
    font-family: "Lato", Arial, sans-serif;
  }
  .business-card {
    position: absolute; left: 100px; top: 225px;
    width: 1000px; height: 572px;
    border-radius: 22px; overflow: hidden;
    background: var(--card-white);
    box-shadow: 0 18px 40px rgba(0,0,0,0.22);
  }
  .card-shape { position: absolute; inset: 0; }
  .brand {
    position: absolute; left: 70px; top: 250px; width: 400px;
    display: flex; align-items: center; gap: 16px;
  }
  .brand-dot {
    width: 34px; height: 34px; border-radius: 50%;
    background: var(--accent-red); flex: none;
  }
  .brand-name {
    font-size: 38px; font-weight: 700; color: var(--accent-red);
    line-height: 1.1; white-space: nowrap;
  }
  .contact {
    position: absolute; right: 130px; top: 82px;
    text-align: right; color: var(--text-light);
  }
  .contact-name {
    font-size: 36px; font-weight: 700; letter-spacing: 1px;
    color: var(--name-yellow); line-height: 46px;
  }
  .contact-role {
    font-size: 23px; color: var(--text-muted); margin: 4px 0 18px 0;
  }
  .contact-line {
    font-size: 24px; line-height: 1.5;
    position: relative; white-space: nowrap;
  }
  .contact-line .icon {
    position: absolute; right: -40px; top: 9px; width: 20px; height: 20px;
  }
  .name-tab {
    position: absolute; right: 0; top: 82px; width: 100px; height: 46px;
    background: var(--accent-red);
  }
  .name-tab::before {
    content: ""; position: absolute; left: 0; top: 0; bottom: 0; width: 10px;
    background: var(--card-white);
  }
</style>
</head>
<body>
  <div class="business-card">
    <svg class="card-shape" viewBox="0 0 1000 572" preserveAspectRatio="none" aria-hidden="true">
      <path d="M470 0 C590 120 620 420 540 572 L1000 572 L1000 0 Z" fill="var(--card-black)"/>
      <path d="M452 0 C572 120 602 420 522 572" fill="none" stroke="var(--accent-red)" stroke-width="6"/>
    </svg>

    <div class="brand">
      <span class="brand-dot"></span>
      <span class="brand-name">Tamarindo Market</span>
    </div>

    <div class="name-tab"></div>

    <div class="contact">
      <p class="contact-name">DANIEL REYES</p>
      <p class="contact-role">Owner</p>
      <p class="contact-line">2465 Calloway Blvd</p>
      <p class="contact-line">Larkfield, MD 21290</p>
      <p class="contact-line">951.555.0140
        <svg class="icon" viewBox="0 0 24 24" aria-hidden="true"><path fill="var(--name-yellow)" d="M6.6 10.8a15 15 0 0 0 6.6 6.6l2.2-2.2a1 1 0 0 1 1-.25 11.4 11.4 0 0 0 3.6.6 1 1 0 0 1 1 1V20a1 1 0 0 1-1 1A17 17 0 0 1 3 4a1 1 0 0 1 1-1h3.5a1 1 0 0 1 1 1c0 1.250.2 2.45.6 3.6a1 1 0 0 1-.25 1z"/></svg>
      </p>
      <p class="contact-line">951.555.0188
        <svg class="icon" viewBox="0 0 24 24" aria-hidden="true"><rect x="3" y="8" width="18" height="11" rx="2" fill="var(--name-yellow)"/><rect x="7" y="3" width="10" height="6" fill="var(--name-yellow)"/></svg>
      </p>
    </div>
  </div>
</body>
</html>
```